Powerpoint Template needed for new Digital Consultancy

We have recently had our logo designed through Sketchmarket and would now like to extend the brand look & feel through to having a powerpoint template created that we can use as a master template within which to create our client presentations.
Typical slides required and in terms of what we would need templating is:

- Stylised header and footer for main content slides
- intro/front page slide
- contents page slide
- standardised font type and sizes, heading types (including sizes) for Level 1, Level 2 and Level 3 headings
- use of text colour and any standards/styling around when to use bold, underline, italics etc
- table styling for when we want to use tables in the presentation
- standards and styles around using bullet and number lists
- stylising use of imagery that is dropped in e.g. do all images have a certain border style or drop-shadow etc.
- style and slide layout/format for how team profiles are handled
- style and slide layout/format for how case studies are handled
- closing, contact-us page

We can send over logo files and colour/font styles etc used for the logo soon.

Target Market(s)

B2B professional clients that are either medium to large corporations or potentially some government departments.

Industry/Entity Type

Digital

Font styles to use
Sans Serif

Colors
ec1f27
f37122
f78f20
faa54b
f68d4d
0255a3

Requirements
Must have
• Ideally as many templated pages/master slide types as outlined above in the brief to meet the requirements of what the powerpoint deck will be used for. Namely client presentations and pitches.
• Versions of the logo are attached to give an idea of the colour palette and clean, modern style we are looking for, plus the type of font we are using and like.
• We are looking for the slide design to be modern, minimalistic, clean and not overuse of colour. Preferably a white slide background so it's easy to then read slide content when we populate the slides with text which will be in black.
Nice to have
• Not expecting to see too much more than simple use of the logo and a slide header perhaps using some sort of line as a break and then a simple footer as well.
• Consider using Abode font.
Should not have
• Too much block colour or elements that draw away from what will go in the main content body of our slides when we use them.

```html
<!DOCTYPE html>
<html lang="en">
<head>
<meta charset="utf-8">
<title>Brightloop slide master</title>
<link rel="stylesheet" href="https://fonts.googleapis.com/css2?family=Open+Sans:wght@400;600&family=Oswald:wght@500&display=swap">
<style>
  :root{
    --red:#ec1f27;
    --title:#e5533d;
    --orange:#f37122;
    --amber:#f78f20;
    --peach:#faa54b;
    --map:#fbcfb0;
    --rule:#e98d84;
    --band:#f1f1f1;
    --ink:#333333;
    --divider:#111111;
    --white:#ffffff;
  }
  *{box-sizing:border-box;margin:0;padding:0}
  html,body{width:1200px;height:918px;overflow:hidden;background:var(--white)}
  body{font-family:"Open Sans",Arial,sans-serif;color:var(--ink);position:relative}
  h1,h2{font-weight:400}
  .sheet{position:relative;width:1200px;height:918px}
  .divider-v{position:absolute;left:600px;top:0;width:1px;height:918px;background:var(--divider)}
  .divider-h{position:absolute;left:0;top:459px;width:1200px;height:1px;background:var(--divider)}
  .slide{position:absolute;width:600px;height:459px;overflow:hidden}
  .slide--cover{left:0;top:0}
  .slide--content{left:600px;top:0}
  .slide--case{left:0;top:459px}
  .slide--table{left:600px;top:459px}

  /* header */
  .header-rule{position:absolute;left:33px;top:80px;width:1px;height:58px;background:var(--rule)}
  .slide-title{position:absolute;left:46px;top:88px;font-size:24px;line-height:32px;color:var(--title)}

  /* footer */
  .footer-rule{position:absolute;left:28px;width:460px;height:1px;background:var(--rule)}
  .page-no{position:absolute;left:22px;width:13px;height:13px;border-radius:50%;background:var(--red);color:var(--white);font-size:6px;line-height:13px;text-align:center}
  .footer-end{position:absolute;left:485px;width:7px;height:7px;border-radius:50%;background:var(--red)}
  .footer-brand{position:absolute;left:494px;font-size:14px;line-height:18px;font-weight:600;color:var(--orange);letter-spacing:-.2px}

  /* cover */
  .map{position:absolute;left:110px;top:64px;width:370px;height:200px;border-radius:40px;background:linear-gradient(135deg,#fcd9c0,var(--map))}
  .cover-rule{position:absolute;left:0;top:205px;width:600px;height:1px;background:var(--rule)}
  .cover-brand{position:absolute;left:0;right:0;top:218px;text-align:center;font-size:46px;line-height:56px;font-weight:600;color:var(--orange);letter-spacing:-1px}
  .cover-title{position:absolute;left:0;right:0;top:286px;text-align:center;font-size:28px;line-height:38px;color:var(--title)}
  .cover-subtitle{position:absolute;left:0;right:0;top:326px;text-align:center;font-size:13px;line-height:18px;color:var(--amber)}

  /* content */
  .body-copy{position:absolute;left:50px;top:140px;width:315px;font-size:10.5px;line-height:14.4px;text-align:justify;color:#444}
  .body-copy p+p{margin-top:11px}
  .lead{color:var(--amber)}
  .feature-badge{position:absolute;left:412px;top:159px;width:94px;height:94px;border-radius:50%;background:var(--orange)}
  .feature-label{position:absolute;left:380px;width:158px;top:280px;text-align:center;font-family:"Oswald","Arial Narrow",sans-serif;font-weight:500;font-size:20px;line-height:28px;color:var(--orange)}

  /* case */
  .case-band{position:absolute;left:0;top:191px;width:592px;height:143px;background:var(--band)}
  .case-badge{position:absolute;left:258px;top:159px;width:77px;height:77px;border-radius:50%;background:var(--orange)}
  .case-copy{position:absolute;left:66px;top:244px;width:460px;font-size:8.6px;line-height:12px;text-align:center;color:#444}
  .case-accent{position:absolute;left:276px;top:334px;width:39px;height:4px;background:var(--orange)}

  /* tables */
  .data-card{position:absolute;top:150px;width:250px;height:190px;background:var(--white);box-shadow:0 0 0 1px #eeeeee}
  .data-card--primary{left:44px}
  .data-card--secondary{left:310px}
  .data-table{width:234px;margin:5px 8px 0;border-collapse:collapse;font-size:5.6px;line-height:7px;text-align:center}
  .data-table th{color:var(--white);font-weight:600;height:26px;padding:0 3px}
  .data-card--primary th{background:var(--orange)}
  .data-card--secondary th{background:var(--peach)}
  .data-table td{height:29px;border-bottom:1px solid #eeeeee;padding:0 3px;color:#444}
  .data-table .wide{width:45%;text-align:left}
  .card-note{position:absolute;left:0;bottom:0;width:100%;height:30px;background:#e6e6e6;font-size:5.8px;line-height:8px;text-align:center;padding:6px 20px;color:#555}
</style>
</head>
<body>
<div class="sheet">

  <section class="slide slide--cover">
    <div class="map" role="img" aria-label="World map in soft peach"></div>
    <div class="cover-rule"></div>
    <div class="cover-brand">Brightloop</div>
    <h1 class="cover-title">Presentation Title here</h1>
    <p class="cover-subtitle">Presentation subtitle here</p>
  </section>

  <section class="slide slide--content">
    <div class="header-rule"></div>
    <h2 class="slide-title">Content Slide</h2>
    <div class="body-copy">
      <p><span class="lead">Lorem ipsum dolor sit amet,</span> consectetur adipiscing elit. Etiam ornare velit at sem euismod, ut pellentesque odio sodales. Ut id rutrum lacus. Phasellus in laoreet dolor. Sed ac nunc fermentum, varius sem vitae, bibendum dui. Pellentesque dictum, sapien vitae ornare volutpat, leo sem cursus lectus, non imperdiet mauris tellus quis eros. Cras dapibus nisl nec mauris elementum, in consequat velit mollis. Donec sit amet gravida justo, ut dapibus elit.</p>
      <p><span class="lead">Lorem ipsum dolor sit amet,</span> consectetur adipiscing elit. Etiam ornare velit at sem euismod, ut pellentesque odio sodales. Ut id rutrum lacus. Phasellus in laoreet dolor. Sed ac nunc fermentum, varius sem vitae, bibendum dui. Pellentesque dictum, sapien vitae ornare volutpat, leo sem cursus lectus,</p>
    </div>
    <div class="feature-badge">
      <svg width="94" height="94" viewBox="0 0 88 88" aria-hidden="true">
        <g fill="none" stroke="#fff" stroke-width="1.8">
          <rect x="32" y="30" width="24" height="30"/>
          <line x1="28" y1="60" x2="60" y2="60"/>
          <line x1="32" y1="36" x2="56" y2="36"/>
          <rect x="37" y="40" width="4" height="4"/><rect x="47" y="40" width="4" height="4"/>
          <rect x="37" y="48" width="4" height="4"/><rect x="47" y="48" width="4" height="4"/>
          <rect x="41" y="54" width="6" height="6"/>
        </g>
      </svg>
    </div>
    <div class="feature-label">LOREM IPSUM</div>
    <div class="footer-rule" style="top:362px"></div>
    <div class="page-no" style="top:356px">2</div>
    <div class="footer-end" style="top:359px"></div>
    <div class="footer-brand" style="top:365px">Brightloop</div>
  </section>

  <section class="slide slide--case">
    <div class="header-rule"></div>
    <h2 class="slide-title">Case Slide</h2>
    <div class="case-band"></div>
    <div class="case-badge">
      <svg width="77" height="77" viewBox="0 0 77 77" aria-hidden="true">
        <g fill="none" stroke="#fff" stroke-width="2.2">
          <circle cx="38.5" cy="38.5" r="11"/>
          <line x1="38.5" y1="22" x2="38.5" y2="31"/><line x1="38.5" y1="46" x2="38.5" y2="55"/>
          <line x1="22" y1="38.5" x2="31" y2="38.5"/><line x1="46" y1="38.5" x2="55" y2="38.5"/>
        </g>
      </svg>
    </div>
    <p class="case-copy">Lorem ipsum dolor sit amet, porttitor adipiscing ipsum, turpis amet wisi molestie pharetra, justo quam. Fermentum wisi ultricies morbi at amet nonummy, id rhoncus, risus duis morbi amet ligula arcu mauris. Eros ut metus, magna mollis eu eros aliquet, laoreet wisi lorem ac similique, amet integer et tellus vitae quam blandit. Elit sed ante id elit. Non id porta vitae vitae. Mauris amet aliquam sit cursus, mauris placerat quis, pellentesque nec, bibendum praesent eget elementum metus sed. Et ante eget eget quam sollicitudin, parturient porttitor, aptent egestas sed aut augue, massa mattis ante blandit, lacus pede accumsan et diam arcu cras</p>
    <div class="case-accent"></div>
    <div class="footer-rule" style="top:373px"></div>
    <div class="page-no" style="top:367px">3</div>
    <div class="footer-end" style="top:370px"></div>
    <div class="footer-brand" style="top:376px">Brightloop</div>
  </section>

  <section class="slide slide--table">
    <div class="header-rule"></div>
    <h2 class="slide-title">Table slide</h2>

    <div class="data-card data-card--primary">
      <table class="data-table">
        <tr><th>Lorem Ipsum</th><th>Lorem Ipsum</th><th>Lorem Ipsum</th><th class="wide">Lorem Ipsum</th></tr>
        <tr><td>Text</td><td>Text</td><td>Text</td><td class="wide">Lorem ipsum dolor sit amet, porttitor adipiscing ipsum.</td></tr>
        <tr><td>Text</td><td>Text</td><td>Text</td><td class="wide">Lorem ipsum dolor sit amet, porttitor adipiscing ipsum.</td></tr>
        <tr><td>Text</td><td>Text</td><td>Text</td><td class="wide">Lorem ipsum dolor sit amet, porttitor adipiscing ipsum.</td></tr>
        <tr><td>Text</td><td>Text</td><td>Text</td><td class="wide">Lorem ipsum dolor sit amet, porttitor adipiscing ipsum.</td></tr>
      </table>
      <p class="card-note">Lorem ipsum dolor sit amet, porttitor adipiscing ipsum, turpis amet wisi molestie pharetra, justo quam.</p>
    </div>

    <div class="data-card data-card--secondary">
      <table class="data-table">
        <tr><th>Lorem Ipsum</th><th>Lorem Ipsum</th><th>Lorem Ipsum</th><th class="wide">Lorem Ipsum</th></tr>
        <tr><td>Text</td><td>Text</td><td>Text</td><td class="wide">Lorem ipsum dolor sit amet, porttitor adipiscing ipsum.</td></tr>
        <tr><td>Text</td><td>Text</td><td>Text</td><td class="wide">Lorem ipsum dolor sit amet, porttitor adipiscing ipsum.</td></tr>
        <tr><td>Text</td><td>Text</td><td>Text</td><td class="wide">Lorem ipsum dolor sit amet, porttitor adipiscing ipsum.</td></tr>
        <tr><td>Text</td><td>Text</td><td>Text</td><td class="wide">Lorem ipsum dolor sit amet, porttitor adipiscing ipsum.</td></tr>
      </table>
      <p class="card-note">Lorem ipsum dolor sit amet, porttitor adipiscing ipsum, turpis amet wisi molestie pharetra, justo quam.</p>
    </div>

    <div class="footer-rule" style="top:373px"></div>
    <div class="page-no" style="top:367px">4</div>
    <div class="footer-end" style="top:370px"></div>
    <div class="footer-brand" style="top:376px">Brightloop</div>
  </section>

  <div class="divider-v"></div>
  <div class="divider-h"></div>
</div>
</body>
</html>
```